Water Delivery Service Website

We are working with BrivoNeté. They are a water delivery company and in need of a new website design.
Some sites to use for inspiration:
https://www.corvindale.example/home
https://www.plumtidego.example/en/home3
https://www.zelkop.example
https://www.hestrova.example
Thank you for taking the time to consider designing a website for us. We are web developers based in Stockton, CA, USA. Most of our projects go through the same process. Understanding this process may help you win a project with us. We custom-code all of our websites in-house. We don’t have any requirements as to what tools you use for your design, but we prefer Figma files. For any design that we label as four-stars, we send it to the client for review. The client picks the final design they want us to use. Once we complete this process, we will continue to show additional clients all the four-star sites and purchase them later. Your designs will have multiple chances to sell. For better chances of success, we ask that you follow these guidelines.
IMAGES:
If you use any images or icons in the design, we ask that you have a link to the asset so we can purchase the image/icon. Most of the designs we submit do not have the customer’s images on them unless they have some great images. Be creative; show us the feeling you are trying to portray with your image choices. Use any royalty-free site you choose. We subscribe to Quenlix and mainly use their images, but we can purchase images outside of Quenlix.
PLEASE NOTE: we will not submit designs to clients with watermarks on the images.
FONTS:
We ask that you identify the fonts used in the design. This can be done in a message if you want. We typically use Google Fonts and Quenlix Fonts.
CONTENT:
We're always open to different content and ideas. We often submit designs with stock images so the client can see our vision. We typically take pictures after the website launch to use their images with our vision. Lorem Ipsum is fine for paragraphs, but we ask that you write the headers in correct English. We want to be able to show the vision and identify the sections of the website.
INSPIRATION:
We typically add a couple of links in the brief of websites we like to help you get started in your design.
REVISIONS:
We do not often ask for revisions of the designs unless we see something in the design that may not appeal to the client. If there are slight changes that we want to make, we do that in the development process.
FEEDBACK:
We rarely give feedback on designs during the design process. We are working on many website projects and do not have the time to provide feedback. We usually respond if your request is well thought out and asks specific questions, but a note asking “feedback, please” usually goes unanswered.

```html
<!DOCTYPE html>
<html lang="en">
<head>
<meta charset="utf-8">
<title>BrivoNeté Water Delivery</title>
<link href="https://fonts.googleapis.com/css2?family=Poppins:wght@400;500;600;700&display=swap" rel="stylesheet">
<style>
:root{
  --blue:#1f5ad8;
  --sky:#2aa7e8;
  --navy:#1d2b57;
  --ink:#1b1b1b;
  --muted:#3c3c3c;
  --soft:#f2f2f3;
  --line:#d9d9d9;
  --white:#ffffff;
}
*{margin:0;padding:0;box-sizing:border-box}
html,body{width:1200px;height:4768px;overflow:hidden}
body{font-family:"Poppins",sans-serif;color:var(--ink);background:var(--white);position:relative}
section,footer{position:relative;width:1200px}
.abs{position:absolute}
.btn{position:absolute;display:inline-flex;align-items:center;justify-content:center;border-radius:20px;font-size:12px;font-weight:600;background:var(--navy);color:var(--white);height:28px;padding:0 16px}
.h2{color:var(--blue);font-weight:600;font-size:40px;line-height:1.25}
.eyebrow{font-size:11px;font-weight:600;letter-spacing:1px;text-transform:uppercase;color:var(--navy)}

/* hero */
.hero{height:643px;overflow:hidden}
.hero-photo{position:absolute;inset:0;background:linear-gradient(100deg,#3f4a55 0%,#6d7986 35%,#c7a98f 65%,#e2c2a7 100%)}
.topbar{position:absolute;top:8px;left:63px;right:63px;display:flex;justify-content:space-between;color:var(--white);font-size:12px}
.topbar .info{display:flex;gap:24px;align-items:center}
.topbar .info span{display:flex;align-items:center;gap:6px}
.topbar .soc{display:flex;gap:12px}
.topbar .soc i{width:14px;height:14px;border-radius:50%;background:var(--white);display:block}
.nav{position:absolute;top:38px;left:63px;width:1075px;height:75px;background:var(--white);border-radius:14px;display:flex;align-items:center;padding:0 18px 0 26px}
.brand{display:flex;align-items:center;gap:8px;font-size:24px;font-weight:600;color:var(--blue)}
.brand i{width:20px;height:20px;border-radius:50%;background:var(--sky);display:block}
.nav ul{list-style:none;display:flex;gap:38px;margin-left:104px;font-size:13px;font-weight:500}
.nav .cart{margin-left:auto;margin-right:16px}
.nav .cta{position:static;background:var(--sky);height:30px;font-size:12px}
.hero .eyebrow{top:216px;left:65px;color:var(--white);text-transform:none;letter-spacing:.5px}
.hero h1{position:absolute;top:242px;left:63px;width:600px;color:var(--white);font-size:40px;font-weight:600;line-height:1.25}
.hero p{position:absolute;top:355px;left:65px;width:520px;color:var(--white);font-size:12px;line-height:1.55}
.hero .b1{top:425px;left:63px;background:var(--navy)}
.hero .b2{top:425px;left:178px;background:var(--white);color:var(--navy)}
.wave-band{position:absolute;left:0;bottom:0;width:1200px;height:120px;background:linear-gradient(180deg,rgba(108,196,240,0) 0%,#4fb0ea 35%,#2f8fd8 65%,#1f67c9 100%)}

/* solutions */
.solutions{height:662px}
.solutions .eyebrow{top:62px;width:100%;text-align:center;text-transform:none;letter-spacing:.5px}
.solutions .h2{position:absolute;top:82px;width:100%;text-align:center}
.sol-card{position:absolute;top:210px;width:236px;text-align:center}
.sol-img{width:236px;height:236px;background:linear-gradient(160deg,#9fb3c3,#4b6b84)}
.sol-card h3{margin-top:18px;color:var(--blue);font-size:14px;font-weight:600}
.sol-card p{margin:12px auto 0;width:220px;font-size:12px;line-height:1.6;color:var(--muted)}
.sol-card .btn{position:static;margin-top:12px}

/* why */
.why{height:350px;background:var(--soft);border-top:1px solid var(--line);border-bottom:1px solid var(--line)}
.why .h2{position:absolute;top:34px;width:100%;text-align:center}
.why-item{position:absolute;top:105px;width:225px;text-align:center}
.why-icon{width:64px;height:64px;border-radius:50%;margin:0 auto;background:linear-gradient(135deg,#9b3cf0,#3a7bf0);display:flex;align-items:center;justify-content:center}
.why-item h3{margin-top:20px;font-size:14px;font-weight:600;color:var(--navy)}
.why-item p{margin:20px auto 0;width:195px;font-size:12px;line-height:1.55;color:var(--muted)}
.vline{position:absolute;top:130px;width:1px;height:165px;background:#9a9a9a}

/* projects */
.projects{height:1185px}
.projects .h2{position:absolute;top:70px;width:100%;text-align:center}
.prod{position:absolute;width:312px;height:390px;background:var(--soft);border-radius:8px;box-shadow:0 4px 6px rgba(0,0,0,.18);text-align:center;padding-top:14px}
.prod-img{width:260px;height:236px;margin:0 auto;background:#e6eef6}
.prod .price{margin-top:18px;font-size:20px;font-weight:600}
.prod .name{margin-top:12px;font-size:12px;color:var(--muted)}
.prod .btn{position:static;margin-top:14px}

/* testimonials */
.testi{height:565px;background:var(--soft)}
.testi .eyebrow{top:52px;left:60px}
.testi .h2{position:absolute;top:76px;left:60px;width:560px}
.testi .lead{position:absolute;top:84px;left:640px;width:490px;font-size:14px;line-height:1.6;color:var(--muted)}
.tcard{position:absolute;top:210px;width:506px;height:280px;border-radius:12px;background:linear-gradient(180deg,#2aa7e8,#2a4fb8);color:var(--white)}
.tcard .q{position:absolute;top:24px;left:28px;font-size:58px;font-weight:700;line-height:1}
.tcard .av{position:absolute;top:38px;left:82px;width:96px;height:96px;border-radius:50%;background:linear-gradient(160deg,#e7c9a8,#8b6a4f)}
.tcard .nm{position:absolute;top:60px;left:210px;font-size:30px;font-weight:600}
.tcard .st{position:absolute;top:102px;left:210px;color:#f5c542;font-size:14px;letter-spacing:2px}
.tcard h4{position:absolute;top:148px;left:82px;font-size:18px;font-weight:500}
.tcard p{position:absolute;top:182px;left:82px;width:330px;font-size:12px;line-height:1.55}
.dots{position:absolute;top:522px;left:566px;display:flex;gap:6px}
.dots i{width:10px;height:10px;border-radius:50%;background:#cfcfcf;display:block}
.dots i:first-child{background:var(--ink)}

/* blog */
.blog{height:695px}
.blog .eyebrow{top:68px;left:60px}
.blog .h2{position:absolute;top:90px;left:60px}
.blog .lead{position:absolute;top:100px;left:755px;width:395px;font-size:14px;line-height:1.55;color:var(--muted)}
.post{position:absolute;top:215px;width:340px;height:392px;border:1px solid var(--line);background:var(--white);padding:12px}
.post-img{width:100%;height:205px;background:linear-gradient(160deg,#c9d6de,#6c8ca3)}
.post h3{margin-top:14px;font-size:15px;font-weight:600;line-height:1.45;color:var(--navy)}
.meta{margin-top:8px;display:flex;gap:14px;font-size:10px;font-weight:500}
.meta span{display:flex;align-items:center;gap:5px}
.meta i{width:10px;height:10px;border-radius:2px;background:var(--navy);display:block}
.post p{margin-top:10px;font-size:12px;line-height:1.5;color:var(--muted)}
.post .rm{margin-top:14px;font-size:13px;font-weight:600;color:var(--navy)}

/* cta */
.cta-band{height:338px;background:linear-gradient(100deg,#1b3d8f 0%,#2f5fb8 45%,#a6bfe3 75%,#2a55a8 100%)}
.cta-band h2{position:absolute;top:80px;left:63px;color:var(--white);font-size:40px;font-weight:600;line-height:1.5}
.cta-band .phone{position:absolute;top:235px;left:63px;height:32px;padding:0 16px;border-radius:18px;background:var(--white);display:flex;align-items:center;gap:8px;font-size:14px;font-weight:500}
.cta-people{position:absolute;left:720px;top:-35px;width:380px;height:373px;background:linear-gradient(180deg,rgba(214,227,242,0) 0%,#c7d6ec 25%,#3a63b8 100%)}

/* footer */
.foot{height:330px}
.foot .brand{position:absolute;top:52px;left:63px;font-size:32px}
.foot .help{position:absolute;top:128px;left:63px;font-size:14px;line-height:1.55;width:230px}
.fcol{position:absolute;top:45px}
.fcol h4{color:var(--sky);font-size:18px;font-weight:600;margin-bottom:18px}
.fcol li{list-style:none;font-size:14px;margin-bottom:15px;display:flex;align-items:center;gap:16px}
.fcol li i{width:22px;height:22px;border-radius:50%;background:var(--ink);display:block}
.foot .rule{position:absolute;top:292px;left:63px;width:1075px;height:1px;background:#8a8a8a}
.foot .copy{position:absolute;top:305px;width:100%;text-align:center;font-size:12px}
</style>
</head>
<body>

<section class="hero">
  <div class="hero-photo" role="img" aria-label="Woman drinking a glass of fresh water"></div>
  <div class="topbar">
    <div class="info">
      <span><svg width="14" height="14" viewBox="0 0 24 24"><path fill="#fff" d="M12 2a7 7 0 0 0-7 7c0 5 7 13 7 13s7-8 7-13a7 7 0 0 0-7-7zm0 9.5A2.5 2.5 0 1 1 12 6.5a2.5 2.5 0 0 1 0 5z"/></svg>Orlen Quay, Vastrel Bay</span>
      <span><svg width="14" height="14" viewBox="0 0 24 24"><path fill="#fff" d="M6.6 10.8a15 15 0 0 0 6.6 6.6l2.2-2.2a1 1 0 0 1 1-.25 11 11 0 0 0 3.6.6 1 1 0 0 1 1 1V20a1 1 0 0 1-1 1A17 17 0 0 1 3 4a1 1 0 0 1 1-1h3.5a1 1 0 0 1 1 1c0 1.25.2 2.45.6 3.6a1 1 0 0 1-.25 1z"/></svg>555-014-2277</span>
    </div>
    <div class="soc"><i></i><i></i><i></i><i></i></div>
  </div>
  <nav class="nav">
    <div class="brand"><i></i>BrivoNeté</div>
    <ul><li>About</li><li>Shop</li><li>Services</li><li>Resources</li><li>Blog</li><li>Contact</li></ul>
    <svg class="cart" width="20" height="20" viewBox="0 0 24 24" fill="none" stroke="#555" stroke-width="1.8"><path d="M3 4h2l2.5 11h11L21 7H6.5"/><circle cx="9" cy="19" r="1.5"/><circle cx="17" cy="19" r="1.5"/></svg>
    <span class="btn cta">Get Water Delivery</span>
  </nav>
  <div class="eyebrow abs">Welcome to BrivoNeté</div>
  <h1>Trusted Water Services for Your Home and Business</h1>
  <p>we are committed to providing high-quality water services that meet the needs of both residential and commercial clients. Our team of experienced professionals ensures safe, clean, and reliable water solutions that you can count on every day.</p>
  <span class="btn b1">Get A Quote</span>
  <span class="btn b2">Our Services</span>
  <div class="wave-band" role="img" aria-label="Decorative blue water waves along the bottom of the banner"></div>
</section>

<section class="solutions">
  <div class="eyebrow abs">Welcome to Tessaly Water</div>
  <h2 class="h2">Clean, Refreshing, and<br>Convenient Water Solutions</h2>
  <div class="sol-card" style="left:60px;top:210px">
    <div class="sol-img" role="img" aria-label="Technician working on water filtration equipment"></div>
    <h3>Water Filtration Systems</h3>
    <p>The convenience of Tessaly Water's home and office delivery service.</p>
    <span class="btn">Read More.</span>
  </div>
  <div class="sol-card" style="left:341px;top:216px">
    <div class="sol-img" role="img" aria-label="Delivery worker loading water bottles"></div>
    <h3>Water Delivery Service</h3>
    <p>Tessaly Water offers state-of-the-art filtration systems that remove..</p>
    <span class="btn">Read More</span>
  </div>
  <div class="sol-card" style="left:623px;top:216px">
    <div class="sol-img" role="img" aria-label="Young tree growing beside water droplets" style="background:linear-gradient(160deg,#7fae6a,#1f4a2a)"></div>
    <h3>Eco-Friendly Solutions</h3>
    <p>At Tessaly Water, we believe in sustainability.</p>
    <span class="btn">Read More</span>
  </div>
  <div class="sol-card" style="left:903px;top:216px">
    <div class="sol-img" role="img" aria-label="Two colleagues talking beside an office water dispenser" style="background:linear-gradient(160deg,#eef0f2,#b9c2cb)"></div>
    <h3>Water Dispensers</h3>
    <p>Tessaly Water also provides top-of-the-line water dispensers.</p>
    <span class="btn">Read More</span>
  </div>
</section>

<section class="why">
  <h2 class="h2">Why Choose BrivoNeté?</h2>
  <div class="why-item" style="left:33px"><div class="why-icon"><svg width="30" height="30" viewBox="0 0 24 24" fill="none" stroke="#fff" stroke-width="1.6"><circle cx="12" cy="8" r="4"/><path d="M4 21c0-4 4-6 8-6s8 2 8 6"/></svg></div><h3>Experienced Professionals</h3><p>Our team has years of experience in the water services industry.</p></div>
  <div class="vline" style="left:263px"></div>
  <div class="why-item" style="left:262px"><div class="why-icon"><svg width="30" height="30" viewBox="0 0 24 24" fill="none" stroke="#fff" stroke-width="1.6"><circle cx="12" cy="12" r="8"/><path d="M12 7v10M9.5 9.5h4a1.5 1.5 0 0 1 0 3h-3a1.5 1.5 0 0 0 0 3h4"/></svg></div><h3>Affordable Pricing</h3><p>We offer competitive pricing without compromising on quality.</p></div>
  <div class="vline" style="left:487px"></div>
  <div class="why-item" style="left:487px"><div class="why-icon"><svg width="30" height="30" viewBox="0 0 24 24" fill="none" stroke="#fff" stroke-width="1.6"><path d="M12 3l7 3v6c0 4-3 7-7 9-4-2-7-5-7-9V6z"/><path d="M9 12l2 2 4-4"/></svg></div><h3>Quality Assurance</h3><p>We use the latest technology and high-quality materials to ensure long-lasting results.</p></div>
  <div class="vline" style="left:712px"></div>
  <div class="why-item" style="left:712px"><div class="why-icon"><svg width="30" height="30" viewBox="0 0 24 24" fill="none" stroke="#fff" stroke-width="1.6"><circle cx="12" cy="7" r="3"/><path d="M6 20c0-3 3-5 6-5s6 2 6 5M3 12h4M17 12h4"/></svg></div><h3>Customer-Approach</h3><p>We prioritize your needs, offering personalized service tailored to your specific.</p></div>
  <div class="vline" style="left:937px"></div>
  <div class="why-item" style="left:937px"><div class="why-icon"><svg width="34" height="34" viewBox="0 0 24 24" fill="none" stroke="#fff" stroke-width="1.4"><circle cx="12" cy="12" r="8"/><text x="12" y="14.5" font-size="7" fill="#fff" stroke="none" text-anchor="middle" font-family="Poppins,sans-serif">24</text></svg></div><h3>24/7 Availability</h3><p>Water emergencies don't wait for business hours, and neither do we.</p></div>
</section>

<section class="projects">
  <h2 class="h2">Our Project</h2>
  <div class="prod" style="left:60px;top:155px"><div class="prod-img" role="img" aria-label="Product photo: 2 litre bottled water" style="background:#e3edf7"></div><div class="price">$10.55</div><div class="name">BrivoNeté 2 Ltr Bottled Water</div><span class="btn">Add to Cart</span></div>
  <div class="prod" style="left:450px;top:155px"><div class="prod-img" role="img" aria-label="Product photo: 5 litre bottled water" style="background:#dbe8f5"></div><div class="price">$10.55</div><div class="name">BrivoNeté 5 Ltr Bottled Water</div><span class="btn">Add to Cart</span></div>
  <div class="prod" style="left:840px;top:155px"><div class="prod-img" role="img" aria-label="Product photo: 19 litre bottled water" style="background:#d4e4f4"></div><div class="price">$10.55</div><div class="name">BrivoNeté 19 Ltr Bottled Water</div><span class="btn">Add to Cart</span></div>
  <div class="prod" style="left:60px;top:623px"><div class="prod-img" role="img" aria-label="Product photo: two 2 litre water bottles" style="background:#e1ebf6"></div><div class="price">$16.55</div><div class="name">BrivoNeté 2 Ltr Combo Bottled Water</div><span class="btn">Add to Cart</span></div>
  <div class="prod" style="left:450px;top:623px"><div class="prod-img" role="img" aria-label="Product photo: reverse osmosis water purifier" style="background:#d6e9f6"></div><div class="price">$16.55</div><div class="name">BrivoNeté 15 Ltr (RO)</div><span class="btn">Add to Cart</span></div>
  <div class="prod" style="left:840px;top:623px"><div class="prod-img" role="img" aria-label="Product photo: water cooler with spare bottle" style="background:#e8ecf0"></div><div class="price">$16.55</div><div class="name">BrivoNeté 2 Ltr Combo Bottled Water</div><span class="btn">Add to Cart</span></div>
  <span class="btn" style="top:1095px;left:553px">View More</span>
</section>

<section class="testi">
  <div class="eyebrow abs">Testimonials</div>
  <h2 class="h2">Here's what our customers say about us</h2>
  <p class="lead">Nullam Eu Nibh Vitae Est Tempor Molestie Id Sed Ex. Quisque Dignissim Maximus Ipsum, Sed Rutrum Metus Tincidunt Et. Sed Eget Tincidunt Ipsum.</p>
  <div class="tcard" style="left:60px">
    <div class="q">“</div>
    <div class="av" role="img" aria-label="Customer portrait"></div>
    <div class="nm">Marlo Venn</div><div class="st">★★★★</div>
    <h4>Five Star Services</h4>
    <p>Lorem Ipsum Dolor Sit Amet, Consectetur Adipiscing Elit, Sed Do Eiusmod Tempor Incididunt Ut Labore Et Dolore Magna Aliqua.</p>
  </div>
  <div class="tcard" style="left:630px">
    <div class="q">“</div>
    <div class="av" role="img" aria-label="Customer portrait"></div>
    <div class="nm">Idra Callow</div><div class="st">★★★★</div>
    <h4 style="top:138px">Reliable Insurence</h4>
    <p style="top:172px">Lorem Ipsum Dolor Sit Amet, Consectetur Adipiscing Elit, Sed Do Eiusmod Tempor Incididunt Ut Labore Et Dolore Magna Aliqua.</p>
  </div>
  <div class="dots"><i></i><i></i><i></i><i></i></div>
</section>

<section class="blog">
  <div class="eyebrow abs">Recent Blog Post</div>
  <h2 class="h2">Stay Update with<br>BrivoNeté</h2>
  <p class="lead">Nullam Eu Nibh Vitae Est Tempor Molestie Id Sed Ex. Quisque Dignissim Maximus Ipsum, Sed Rutrum Metus Tincidunt Et. Sed Eget Tincidunt Ipsum.</p>
  <article class="post" style="left:60px">
    <div class="post-img" role="img" aria-label="Delivery worker carrying a large water bottle"></div>
    <h3>The Benefits Of Drinking<br>Clean, Purified Water</h3>
    <div class="meta"><span><i></i>August 12, 2024</span><span><i style="border-radius:50%"></i>By Admin</span></div>
    <p>Drinking Clean, Purified Water Is Essential For Health And Well-Being. In This Blog,</p>
    <div class="rm">READ MORE...</div>
  </article>
  <article class="post" style="left:430px">
    <div class="post-img" role="img" aria-label="Home water filtration unit with tank" style="background:linear-gradient(160deg,#e9ecef,#9aa6b0)"></div>
    <h3>How Water Filtration<br>Systems Can Improve.</h3>
    <div class="meta"><span><i></i>August 12, 2024</span><span><i style="border-radius:50%"></i>By Admin</span></div>
    <p>Drinking Clean, Purified Water Is Essential For Health And Well-Being. In This Blog,</p>
    <div class="rm">READ MORE...</div>
  </article>
  <article class="post" style="left:800px">
    <div class="post-img" role="img" aria-label="Child drinking from a water bottle outdoors" style="background:linear-gradient(160deg,#9fcf7c,#3f7a3a)"></div>
    <h3>The Environmental Impact Of<br>Bottled Water</h3>
    <div class="meta"><span><i></i>August 12, 2024</span><span><i style="border-radius:50%"></i>By Admin</span></div>
    <p>Drinking Clean, Purified Water Is Essential For Health And Well-Being. In This Blog,</p>
    <div class="rm">READ MORE...</div>
  </article>
</section>

<section class="cta-band">
  <h2>Please Call Us to Take an<br>Extraordinary Service</h2>
  <div class="phone"><svg width="16" height="16" viewBox="0 0 24 24"><path fill="#1b1b1b" d="M6.6 10.8a15 15 0 0 0 6.6 6.6l2.2-2.2a1 1 0 0 1 1-.25 11 11 0 0 0 3.6.6 1 1 0 0 1 1 1V20a1 1 0 0 1-1 1A17 17 0 0 1 3 4a1 1 0 0 1 1-1h3.5a1 1 0 0 1 1 1c0 1.25.2 2.45.6 3.6a1 1 0 0 1-.25 1z"/></svg>555-019-9034</div>
  <div class="cta-people" role="img" aria-label="Customer signing a clipboard beside a delivery worker carrying a water bottle"></div>
</section>

<footer class="foot">
  <div class="brand"><i></i>BrivoNeté</div>
  <p class="help">If You Have Question, Please Use Our 24-7 Hours Helpline</p>
  <div class="fcol" style="left:410px"><h4>Information</h4><ul><li>Home</li><li>About Us</li><li>Services</li><li>Resources</li><li>Blogs</li></ul></div>
  <div class="fcol" style="left:695px"><h4>Social Media</h4><ul><li><i></i>Friendlane</li><li><i></i>Vidora</li><li><i></i>Pictiva</li><li><i></i>Chirpline</li></ul></div>
  <div class="fcol" style="left:976px"><h4>Resources</h4><ul><li>Terms Of Condition</li><li>Privacy Policy</li><li>Cookies</li></ul></div>
  <div class="rule"></div>
  <div class="copy">2025 Copyright © <b>BrivoNeté Water Delivery</b> Inc All Rights Reserved</div>
</footer>

</body>
</html>
```